Business Card & Logo Design - Hedge Fund

We need a business card and logo design for a hedge fund. The hedge fund is named Morvane Equity LLC. Morvane Equity was created by finance professors and the strategy is based academic research that looks for patterns in stock prices. The design should look conservative, solid, strong. We favor a classic style - nothing flashy. The logo can relate to the name Morvane Equity, or it could involve a symbol design that connotes "science" . We are open to ideas. We do not want alot of colors - but if any, color - blue is preferred. The font that seems to look best for the name (Morvane Equity) is arial black. We are open to ideas. Most important - we want to see a mock up of an actual business card with the logo concept embedded. The business card should include space for : company name, individual name, position title, cell phone, address. We hope to have this work done by Sept. 8.

Target Market(s)

We will be meeting with and giving the business card to institutions and high net worth individuals.

Industry/Entity Type

Investment Advisory

Contact Information for Business Card

Company name - Morvane Equity LLC
Individual name - Peter Dalby
Title - Portfolio Manager
Cell - (412) 555-0187
Address - 2650 Birchmont Lane, Suite 300, Atlanta GA 30327

Font styles to use
Other font styles liked:
• Arial

Colors
3277b5
0255a3
85acd3
cedeed
fdf9cf
d9d9d9
e6e6e6
f04a50
6b449b

Requirements
Must have
• Must have card details that are sited above.
• We would like a logo related to the name (Morvane Equity) or concept of the fund.
Nice to have
• We want conservative / understated / clean crisp look.
• If any colors - we prefer conservative appearance - blue / gray.
• I have enclosed an example of a card style that looks attractive - please do not exactly copy this card. This is not our company or logo. I feel the layout is attractive - just as an example
Should not have
• Avoid too much color.
• I have selected some preferred colors. Please do not use all of the colors - I have selected a few that might work - but I am not sure. We are open to your ideas so please do not feel the need to use all or any of these.

```html
<!DOCTYPE html>
<html lang="en">
<head>
<meta charset="utf-8">
<title>Morvane Equity LLC – Business Card</title>
<link href="https://fonts.googleapis.com/css2?family=Archivo+Black&family=Arimo:wght@400;700&display=swap" rel="stylesheet">
<style>
  :root {
    --navy: #15426f;
    --grey: #a9a9a9;
    --grey-text: #8a8a8a;
    --paper: #ffffff;
    --backdrop: #2b2b2b;
  }
  * { box-sizing: border-box; margin: 0; padding: 0; }
  html, body { width: 1200px; height: 880px; overflow: hidden; }
  body { background: var(--backdrop); position: relative; font-family: "Arimo", Arial, sans-serif; }

  .card {
    position: absolute;
    width: 620px;
    height: 354px;
    background: var(--paper);
    border-radius: 22px;
    overflow: hidden;
    box-shadow: 0 14px 30px rgba(0,0,0,0.45);
  }
  .card--front { left: 90px; top: 56px; }
  .card--back { left: 490px; top: 470px; }

  .brand { display: flex; align-items: center; gap: 14px; }
  .brand__mark { width: 44px; height: 44px; border-radius: 50%; background: var(--navy); flex: none; }
  .brand__name {
    font-family: "Archivo Black", "Arial Black", sans-serif;
    color: var(--navy);
    font-size: 26px;
    letter-spacing: 0.2px;
    white-space: nowrap;
  }
  .card--front .brand { position: absolute; left: 50%; top: 50%; transform: translate(-50%, -50%); }
  .card--back .brand { position: absolute; left: 36px; top: 128px; }
  .card--back .brand__name { font-size: 22px; }
  .card--back .brand__mark { width: 38px; height: 38px; }

  .panel {
    position: absolute;
    left: 380px; top: 110px; right: 0; bottom: 0;
    background: var(--navy);
  }
  .rule {
    position: absolute;
    left: 0; bottom: 0;
    width: 380px; height: 10px;
    background: var(--grey);
  }

  .person { position: absolute; right: 30px; top: 30px; text-align: right; }
  .person__name { font-weight: 700; color: var(--navy); font-size: 19px; }
  .person__title { color: var(--grey-text); font-size: 14px; margin-top: 2px; }

  .contact {
    position: absolute; right: 30px; top: 146px;
    color: var(--paper); font-size: 14px; line-height: 1.45;
    text-align: right; font-style: normal;
  }
  .contact__address { margin-bottom: 14px; }
  .contact__line { display: flex; justify-content: flex-end; align-items: center; gap: 8px; }
  .contact__icon { width: 18px; height: 18px; flex: none; }
</style>
</head>
<body>

<section class="card card--front" aria-label="Card front">
  <div class="brand">
    <span class="brand__mark"></span>
    <span class="brand__name">Morvane Equity LLC</span>
  </div>
</section>

<section class="card card--back" aria-label="Card back">
  <div class="panel"></div>
  <div class="rule"></div>

  <div class="brand">
    <span class="brand__mark"></span>
    <span class="brand__name">Morvane Equity LLC</span>
  </div>

  <div class="person">
    <div class="person__name">Peter Dalby</div>
    <div class="person__title">Portfolio Manager</div>
  </div>

  <address class="contact">
    <div class="contact__address">2650 Birchmont Lane<br>Suite 300<br>Atlanta GA 30327</div>
    <div class="contact__line">(412) 555-0187
      <svg class="contact__icon" viewBox="0 0 18 18" aria-hidden="true">
        <circle cx="9" cy="9" r="8" fill="none" stroke="#fff" stroke-width="1.3"/>
        <rect x="6" y="4" width="6" height="10" rx="1.2" fill="none" stroke="#fff" stroke-width="1.2"/>
      </svg>
    </div>
    <div class="contact__line">info@morvaneequity.com
      <svg class="contact__icon" viewBox="0 0 18 18" aria-hidden="true">
        <circle cx="9" cy="9" r="8" fill="none" stroke="#fff" stroke-width="1.3"/>
        <rect x="5" y="6" width="8" height="6" fill="none" stroke="#fff" stroke-width="1.1"/>
        <path d="M5 6 L9 9.5 L13 6" fill="none" stroke="#fff" stroke-width="1.1"/>
      </svg>
    </div>
  </address>
</section>

</body>
</html>
```